BrightWanderDoc.com Blog Design (Travel, Lifestyle, and Life Hacking blog)

I am launching a lifestyle blog about my life. I'm a doctor who travels the world trying the best restaurants, airlines and trying to have as much fun as possible. I also invest in startups, and am always trying new tricks to make life better. I also plan to write about various other topics, but essentially it is about travel, lifestyle and medicine. I need a creative and really awesome looking design for a new wordpress blog called BrightWanderDoc

Target Market(s)

Physicians, Entrepreneurs, Travellers

Industry/Entity Type

Airlines

Number of Pages Required

1 page

Font styles to use
Serif

Requirements
Must have
• Slick looking graphics with a highly professional modern feel

```html
<!DOCTYPE html>
<html lang="en">
<head>
<meta charset="utf-8">
<title>BrightWanderDoc.com – Travel, Lifestyle &amp; Medicine</title>
<link href="https://fonts.googleapis.com/css2?family=Montserrat:wght@400;500;600;700&family=Open+Sans:wght@400;600&display=swap" rel="stylesheet">
<style>
:root{
  --green:#78b52c;
  --green-dark:#75a620;
  --blue:#2b80d6;
  --blue-deep:#1f63b0;
  --ink:#1e1e1e;
  --text:#555;
  --muted:#8a8a8a;
  --line:#e2e2e2;
  --orange:#f07d1a;
  --white:#fff;
}
*{margin:0;padding:0;box-sizing:border-box}
html,body{width:1200px;height:2597px;overflow:hidden;background:var(--white)}
body{font-family:"Open Sans",Arial,sans-serif;color:var(--text)}
.page{position:relative;width:1200px;height:2597px;overflow:hidden;
  background:linear-gradient(180deg,#e9f1f8 0,#f4f8fb 320px,#fff 620px,#fff 100%)}
.abs{position:absolute}
.sky{left:0;top:0;width:1200px;height:600px;
  background:radial-gradient(ellipse at 50% 0,#cfdeec 0,#e6eef6 40%,rgba(255,255,255,0) 75%)}
.brand{left:204px;top:50px;font-family:"Montserrat",sans-serif;font-weight:600;font-size:34px;color:var(--blue);letter-spacing:.5px}
.search{left:788px;top:69px;width:204px;height:29px;border:1px solid #c9c9c9;border-radius:15px;background:#fff;
  font-size:10px;color:#999;padding:7px 14px}
.search svg{position:absolute;right:10px;top:7px}
.nav{left:196px;top:111px;width:812px;height:45px;background:var(--green);display:flex}
.nav a{font-family:"Montserrat",sans-serif;font-size:13px;font-weight:500;color:#fff;text-decoration:none;
  display:flex;align-items:center;justify-content:center;border-right:1px solid rgba(255,255,255,.25)}
.nav a.on{background:var(--blue)}
.hero{left:196px;top:159px;width:812px;height:371px;
  background:linear-gradient(90deg,#5b4a34 0,#7a6a4c 20%,#3f5a3a 45%,#6a7352 70%,#4b4330 100%)}
.hero-fall{left:430px;top:159px;width:80px;height:300px;background:linear-gradient(180deg,#e8ece6,#b7c3b9 70%,rgba(200,210,200,0));opacity:.7}
.hero-title{left:370px;top:286px;width:462px;border-top:1px solid rgba(255,255,255,.8);border-bottom:1px solid rgba(255,255,255,.8);
  text-align:center;color:#fff;font-family:"Montserrat",sans-serif;font-weight:700;padding:8px 0 10px}
.hero-title .l1{font-size:36px;line-height:42px;letter-spacing:.5px}
.hero-title .l2{font-size:26px;line-height:32px}
.arrow{width:25px;height:38px;background:#fff;display:flex;align-items:center;justify-content:center}
.sec-title{font-family:"Montserrat",sans-serif;font-weight:600;font-size:21px;color:var(--ink)}
.top-post{width:398px;height:258px}
.top-post .cap{position:absolute;left:0;bottom:0;width:100%;height:65px;background:rgba(255,255,255,.82);padding:12px 20px}
.top-post h3{font-family:"Montserrat",sans-serif;font-size:16px;font-weight:500;color:var(--ink)}
.top-post p{font-size:11.5px;color:#666;margin-top:6px}
.top-post .corner{position:absolute;right:8px;bottom:8px;width:10px;height:10px;border-right:2px solid var(--blue);border-bottom:2px solid var(--blue)}
.feat-title{font-family:"Montserrat",sans-serif;font-weight:600;font-size:20px;color:var(--blue)}
.card{width:258px}
.card .ph{height:149px;position:relative}
.tag{position:absolute;font-family:"Montserrat",sans-serif;font-size:10.5px;color:#fff;padding:3px 11px;text-transform:uppercase}
.tag.life{background:var(--orange)}
.tag.travel{background:var(--blue)}
.tag.med{background:var(--green)}
.card .kicker{font-family:"Montserrat",sans-serif;font-size:11px;color:#7a5aa8;margin-top:14px;height:16px}
.card .kicker.tagged{height:20px;margin-top:14px}
.card .kicker.tagged span{position:static;display:inline-block}
.card h4{font-family:"Montserrat",sans-serif;font-weight:400;font-size:15px;color:var(--ink);margin-top:9px}
.card p,.item p{font-size:11px;line-height:17.3px;color:#555;margin-top:6px}
.more{font-family:"Montserrat",sans-serif;font-size:11.5px;color:var(--blue);display:block;margin-top:8px}
.about{left:748px;top:959px;width:258px;height:335px;background:linear-gradient(180deg,#3a8fe6,#2a7cd8);overflow:hidden}
.about .ph{position:absolute;left:0;top:0;width:258px;height:150px;background:linear-gradient(160deg,#8bb050,#5f8a3a 60%,#a9b98a)}
.about .curve{position:absolute;left:0;top:120px}
.about h4{position:absolute;top:168px;width:100%;text-align:center;font-family:"Montserrat",sans-serif;font-weight:500;font-size:19px;color:#fff;letter-spacing:.5px}
.about p{position:absolute;top:203px;left:22px;width:214px;text-align:center;font-size:10.5px;line-height:17px;color:#eaf3ff}
.about .btn{position:absolute;left:84px;top:283px;width:100px;height:28px;border:1px solid #fff;color:#fff;font-family:"Montserrat",sans-serif;font-size:10.5px;display:flex;align-items:center;justify-content:center}
.divider{left:194px;top:1299px;width:533px;height:1px;background:var(--line)}
.item-ph{width:260px;height:183px}
.item{width:256px}
.item h4{font-family:"Montserrat",sans-serif;font-weight:600;font-size:15px;line-height:21px;color:var(--blue-deep)}
.item .row{display:flex;justify-content:space-between;align-items:center;margin-top:8px}
.item .row .more{margin-top:0;color:var(--green)}
.shares{display:flex;gap:8px}
.shares i{display:block;width:16px;height:16px;border-radius:50%;background:#e6e6e6}
.widget{left:748px;width:258px;border:1px solid #dcdcdc;background:#fff}
.widget .hd{height:41px;color:#fff;font-family:"Montserrat",sans-serif;font-size:17px;font-weight:500;padding:10px 18px;letter-spacing:.3px}
.tips .hd{background:var(--green)}
.arch .hd{background:var(--blue)}
.tip{position:absolute;left:18px;width:228px}
.tip .ph{height:108px}
.tip h5{font-family:"Montserrat",sans-serif;font-weight:400;font-size:14px;color:var(--ink);margin-top:22px}
.tip p{font-size:10.5px;line-height:17px;color:#555;margin-top:5px}
.tip .more{color:var(--green);margin-top:6px}
.arch ul{list-style:none;padding:18px 0 0 34px}
.arch li{font-size:10.5px;color:#555;height:30px;position:relative}
.arch li::before{content:"";position:absolute;left:-14px;top:4px;width:5px;height:5px;border-top:1px solid #888;border-right:1px solid #888;transform:rotate(45deg)}
.footer{left:0;top:2282px;width:1200px;height:315px;background:var(--green-dark)}
.footer h6{font-family:"Montserrat",sans-serif;font-weight:500;font-size:15px;color:#fff;letter-spacing:.4px}
.footer .links a{position:absolute;font-size:11.5px;color:#f0f6e6;text-decoration:none}
.footer .circ{position:absolute;width:28px;height:28px;border-radius:50%;background:#fff}
.footer .sub{font-size:11px;color:#f0f6e6}
.footer .email{left:715px;top:104px;width:178px;height:31px;background:#fff;font-size:9px;color:#aaa;padding:10px 12px;letter-spacing:.3px}
.footer .go{left:893px;top:104px;width:85px;height:31px;background:#1f8fd9;color:#fff;font-family:"Montserrat",sans-serif;font-weight:600;font-size:10.5px;display:flex;align-items:center;justify-content:center}
.footer .rule{left:202px;top:250px;width:796px;height:1px;background:rgba(255,255,255,.3)}
.footer .copy{left:0;top:265px;width:1200px;text-align:center;font-size:10px;color:#dbe9c4}
</style>
</head>
<body>
<div class="page">
  <div class="abs sky" role="img" aria-label="Soft snowy mountain backdrop"></div>

  <header>
    <div class="abs brand">BrightWanderDoc</div>
    <div class="abs search">Search here
      <svg width="13" height="13" viewBox="0 0 13 13"><circle cx="5.5" cy="5.5" r="4.3" fill="none" stroke="#888" stroke-width="1.4"/><line x1="8.6" y1="8.6" x2="12" y2="12" stroke="#888" stroke-width="1.6"/></svg>
    </div>
    <nav class="abs nav">
      <a class="on" style="width:126px">HOME</a>
      <a style="width:113px">ABOUT US</a>
      <a style="width:117px">OUR BLOGS</a>
      <a style="width:105px">ARTICLES</a>
      <a style="width:125px">RESOURCES</a>
      <a style="width:104px">TRAVEL</a>
      <a style="width:122px;border-right:0">CONTACT</a>
    </nav>
  </header>

  <section>
    <div class="abs hero" role="img" aria-label="Waterfall dropping into a green canyon"></div>
    <div class="abs hero-fall" role="img" aria-label="Waterfall mist"></div>
    <div class="abs hero-title"><div class="l1">I M TELLING YOU ABOUT</div><div class="l2">LIFETYLE &amp; TRAVEL</div></div>
    <div class="abs arrow" style="left:190px;top:317px"><svg width="8" height="10"><path d="M6 1 2 5l4 4" fill="none" stroke="#333" stroke-width="1.5"/></svg></div>
    <div class="abs arrow" style="left:984px;top:317px"><svg width="8" height="10"><path d="M2 1l4 4-4 4" fill="none" stroke="#333" stroke-width="1.5"/></svg></div>
  </section>

  <section>
    <h2 class="abs sec-title" style="left:0;width:1200px;text-align:center;top:557px">LATEST TOP POSTS</h2>
    <article class="abs top-post" style="left:194px;top:609px;background:linear-gradient(135deg,#c9d4cf,#8fa88f 50%,#d9ddd6)" role="img" aria-label="Two women jogging in a park">
      <div class="cap"><h3>BLOG TITTLE HERE</h3><p>Praesent elementum elit at tellus nec ultricies sit amet</p></div><span class="corner"></span>
    </article>
    <article class="abs top-post" style="left:610px;top:609px;background:linear-gradient(160deg,#7fb13a,#4f8a22 60%,#9bc560)" role="img" aria-label="Friends lying on green grass">
      <div class="cap"><h3>BLOG TITTLE HERE</h3><p>Praesent elementum elit at tellus nec ultricies sit amet</p></div><span class="corner"></span>
    </article>
  </section>

  <section>
    <h2 class="abs feat-title" style="left:194px;top:917px">FEATURED BLOGS</h2>
    <article class="abs card" style="left:194px;top:959px">
      <div class="ph" style="background:linear-gradient(180deg,#f3b35a,#e98a3a 55%,#6a6f80)" role="img" aria-label="Woman stretching on a beach at sunset"><span class="tag life" style="left:0;bottom:0">Lifestyle</span></div>
      <div class="kicker">LATESET</div>
      <h4>Morbi ornare elit Integer</h4>
      <p>congue augue et malesuada iaculis ipsum dui aliquet felis at cursus magna nisl nec elit Praesent elementum elit at tellus nec ultricies sit amet porttitor mattis enim In massa libero interdum</p>
      <span class="more">READ MORE</span>
    </article>
    <article class="abs card" style="left:471px;top:959px">
      <div class="ph" style="background:linear-gradient(180deg,#b9cbd8,#7d9a86 50%,#8c8a4f)" role="img" aria-label="Hiker overlooking a mountain lake"></div>
      <div class="kicker tagged"><span class="tag travel">Travel</span></div>
      <h4 style="margin-top:5px">Morbi ornare elit Integer</h4>
      <p>congue augue et malesuada iaculis ipsum dui aliquet felis at cursus magna nisl nec elit Praesent elementum elit at tellus nec ultricies sit amet porttitor mattis enim In massa libero interdum</p>
      <span class="more">READ MORE</span>
    </article>
    <aside class="abs about">
      <div class="ph" role="img" aria-label="Portrait of the blog author outdoors"></div>
      <svg class="curve" width="258" height="50" viewBox="0 0 258 50"><path d="M0 30 Q129 -10 258 30 V50 H0Z" fill="#3a8fe6"/></svg>
      <h4>ABOUT ME</h4>
      <p>Aommodo a mi Morbi ornare gravida elit Integer congue augue et malesuada iaculis ipsum dui aliquet felis at cursus magna nisl nec elit Praesent elementum elit</p>
      <span class="btn">READ MORE</span>
    </aside>
    <div class="abs divider"></div>
  </section>

  <section>
    <div class="abs item-ph" style="left:194px;top:1330px;background:linear-gradient(135deg,#f4efe0,#d9c79a 50%,#8ab2c8)" role="img" aria-label="Hands holding a glowing globe"><span class="tag travel" style="left:0;bottom:0">Travel</span></div>
    <article class="abs item" style="left:471px;top:1330px">
      <h4>Cum sociis natoque penatibus et magnis dis parturient</h4>
      <p>congue augue et malesuada iaculis ipsum dui aliquet felis at cursus magna nisl nec elit Praesent elementum elit at tellus nec ultricies sit amet t ac nisl Cum sociis natoque penatibus et magnis dis parturient montes nascetur ridiculus mus In iaculis facilisis massa Etiam eu urna Seddum</p>
      <div class="row"><span class="more">READ MORE</span><div class="shares"><i></i><i></i><i></i><i></i><i></i></div></div>
    </article>

    <div class="abs item-ph" style="left:194px;top:1565px;background:linear-gradient(180deg,#3f86d2,#9fc3e6 40%,#4a6f8a 65%,#2c6fb0)" role="img" aria-label="Snowy peaks above a blue lake"><span class="tag travel" style="left:0;bottom:0">Travel</span></div>
    <article class="abs item" style="left:471px;top:1565px">
      <h4>Nullam enim leo egestas id condiment laoreet</h4>
      <p>congue augue et malesuada iaculis ipsum dui aliquet felis at cursus magna nisl nec elit Praesent elementum elit at tellus nec ultricies sit amet t ac nisl Cum sociis natoque penatibus et magnis dis parturient montes nascetur ridiculus mus In iaculis facilisis massa Etiam eu urna Seddum</p>
      <div class="row"><span class="more">READ MORE</span><div class="shares"><i></i><i></i><i></i><i></i><i></i></div></div>
    </article>

    <div class="abs item-ph" style="left:194px;top:1801px;background:linear-gradient(160deg,#f0d6a8,#c99a62 50%,#6b5a48)" role="img" aria-label="Woman running up outdoor stairs"><span class="tag life" style="left:0;bottom:0">Lifestyle</span></div>
    <article class="abs item" style="left:471px;top:1801px">
      <h4>Nullam enim leo egestas id condiment laoreet</h4>
      <p>congue augue et malesuada iaculis ipsum dui aliquet felis at cursus magna nisl nec elit Praesent elementum elit at tellus nec ultricies sit amet t ac nisl Cum sociis natoque penatibus et magnis dis parturient montes nascetur ridiculus mus In iaculis facilisis massa Etiam eu urna Seddum</p>
      <div class="row"><span class="more">READ MORE</span><div class="shares"><i></i><i></i><i></i><i></i><i></i></div></div>
    </article>

    <div class="abs item-ph" style="left:194px;top:2031px;background:linear-gradient(135deg,#f2ede6,#d8c3b5 50%,#9cb07a)" role="img" aria-label="Herbal remedies and medicine jars"><span class="tag med" style="left:0;bottom:0">Medicine</span></div>
    <article class="abs item" style="left:471px;top:2031px">
      <h4>Nullam enim leo egestas id condiment laoreet</h4>
      <p>congue augue et malesuada iaculis ipsum dui aliquet felis at cursus magna nisl nec elit Praesent elementum elit at tellus nec ultricies sit amet t ac nisl Cum sociis natoque penatibus et magnis dis parturient montes nascetur ridiculus mus In iaculis facilisis massa Etiam eu urna Seddum</p>
      <div class="row"><span class="more">READ MORE</span><div class="shares"><i></i><i></i><i></i><i></i><i></i></div></div>
    </article>
  </section>

  <aside class="abs widget tips" style="top:1339px;height:540px">
    <div class="hd">LATEST TIPS</div>
    <div class="tip" style="top:58px">
      <div class="ph" style="background:linear-gradient(135deg,#5a2a2a,#8a3a2a 40%,#6c8a3a)" role="img" aria-label="Fresh fruit and vegetables"></div>
      <h5>Aommodo Morbi ornare</h5>
      <p>gravida elit Integer congue augue et malesuada iaculis ipsum dui aliquet felis at</p>
      <span class="more">READ MORE</span>
    </div>
    <div class="tip" style="top:288px">
      <div class="ph" style="background:linear-gradient(180deg,#a7b4b8,#7b8a5e 55%,#55603c)" role="img" aria-label="Person doing yoga in the mountains"></div>
      <h5>Aommodo Morbi ornare</h5>
      <p>gravida elit Integer congue augue et malesuada iaculis ipsum dui aliquet felis at</p>
      <span class="more">READ MORE</span>
    </div>
  </aside>

  <aside class="abs widget arch" style="top:1891px;height:329px">
    <div class="hd">ARCHIVES</div>
    <ul>
      <li>June 2015 (3)</li><li>June 2015 (3)</li><li>May 2015 (3)</li><li>April 2015 (2)</li>
      <li>March 2015 (5)</li><li>February 2015 (2)</li><li>January 2015 (1)</li><li>December 2014 (3)</li>
    </ul>
  </aside>

  <footer class="abs footer">
    <h6 class="abs" style="left:206px;top:48px">INFORMATION</h6>
    <div class="links">
      <a style="left:206px;top:80px">Home</a><a style="left:206px;top:106px">About Us</a>
      <a style="left:206px;top:132px">Our Articles</a><a style="left:206px;top:158px">News</a>
      <a style="left:346px;top:80px">Latest Blogs</a><a style="left:346px;top:106px">Archive</a>
      <a style="left:346px;top:132px">Resources</a><a style="left:346px;top:158px">Contact</a>
    </div>
    <h6 class="abs" style="left:497px;top:48px">FOLLOW US</h6>
    <span class="circ" style="left:498px;top:80px"></span>
    <span class="circ" style="left:537px;top:80px"></span>
    <span class="circ" style="left:576px;top:80px"></span>
    <span class="circ" style="left:618px;top:80px"></span>
    <h6 class="abs" style="left:713px;top:48px">SIGN UP FOR NEWSLETTERS</h6>
    <p class="abs sub" style="left:713px;top:77px">Please sign up here for latest news</p>
    <div class="abs email">EMAIL ADDRESS</div>
    <div class="abs go">SUBSCRIBE</div>
    <div class="abs rule"></div>
    <p class="abs copy">© 2016 Company Name. All right reserved. Term of Use</p>
  </footer>
</div>
</body>
</html>
```